Business Card Design

I need a business card design for a new company based in Australind, Western Australia. The business is for puppet shows at children's parties, fetes, custom puppet builds, etc.Attached is a picture of Ray Caldwick in silhouette. I was thinking a design of a puppeteer at the top of some stairs talking to a puppet in silhouette but open to suggestions. (Under the willow is named as I do all my puppet builds in the top room of my house (at the Under the willow).

Industry/Entity Type

Business

Contact Information for Business Card

Under The Willow Puppets, Dale Munroe, Puppeteer / Puppet Builder, phone - 0438215076, Puppet shows / Custom Puppet Builds, Working With Children

Requirements
Must have
• Name and Logo on one side. Second side to have business card details.

```html
<!DOCTYPE html>
<html lang="en">
<head>
<meta charset="utf-8">
<title>Under The Willow Puppets – Business Card</title>
<link rel="stylesheet" href="https://fonts.googleapis.com/css2?family=Comfortaa:wght@400&family=Open+Sans:wght@400;600&display=swap">
<style>
  :root {
    --page-bg: #e9ebee;
    --card-white: #ffffff;
    --ink-dark: #3a3a3a;
    --ink-mid: #555555;
    --brand-blue: #2f7fd6;
    --brand-blue-deep: #1f66bd;
    --divider: #9cc3ee;
  }
  * { box-sizing: border-box; margin: 0; padding: 0; }
  html, body {
    width: 1200px; height: 900px; overflow: hidden;
    background: var(--page-bg);
    font-family: "Open Sans", Arial, sans-serif;
  }
  .sheet {
    width: 1200px; height: 900px;
    display: flex; flex-direction: column;
    align-items: center; justify-content: center; gap: 50px;
  }
  .card {
    position: relative;
    width: 700px; height: 400px;
    background: var(--card-white);
    box-shadow: 0 6px 18px rgba(0,0,0,0.18);
  }
  .card--back { border: 14px solid var(--brand-blue); }

  .brand {
    position: absolute;
    display: flex; align-items: center; gap: 18px;
    white-space: nowrap;
  }
  .card--front .brand { left: 70px; top: 170px; }
  .card--back .brand { left: 56px; top: 112px; }

  .brand__mark {
    flex: none;
    width: 46px; height: 46px; border-radius: 50%;
    background: var(--brand-blue);
  }
  .brand__name {
    font-family: "Comfortaa", "Open Sans", sans-serif;
    font-weight: 400;
    color: var(--ink-dark);
    font-size: 34px;
    letter-spacing: 0.5px;
  }

  .holder {
    position: absolute; right: 392px; top: 238px;
    text-align: right; line-height: 1.2;
  }
  .holder__name { color: var(--brand-blue-deep); font-weight: 600; font-size: 19px; }
  .holder__role { color: var(--ink-mid); font-size: 16px; }

  .divider {
    position: absolute; left: 304px; top: 222px;
    width: 1px; height: 80px;
    background: linear-gradient(to bottom, transparent, var(--divider), transparent);
  }

  .contacts {
    position: absolute; left: 330px; top: 214px;
    list-style: none;
  }
  .contacts__item {
    display: flex; align-items: center; gap: 10px;
    font-size: 16px; color: var(--ink-mid);
    margin-bottom: 8px;
  }
  .contacts__icon {
    width: 22px; height: 22px; border-radius: 3px;
    background: var(--brand-blue);
    display: flex; align-items: center; justify-content: center;
  }
</style>
</head>
<body>
<main class="sheet">
  <section class="card card--front" aria-label="Card front">
    <div class="brand">
      <span class="brand__name">Under The Willow Puppets</span>
      <span class="brand__mark"></span>
    </div>
  </section>

  <section class="card card--back" aria-label="Card back">
    <div class="brand">
      <span class="brand__name">Under The Willow Puppets</span>
      <span class="brand__mark"></span>
    </div>

    <div class="holder">
      <div class="holder__name">Nell Harper</div>
      <div class="holder__role">CEO and Manager</div>
    </div>

    <div class="divider"></div>

    <ul class="contacts">
      <li class="contacts__item">
        <span class="contacts__icon">
          <svg width="14" height="14" viewBox="0 0 24 24"><path fill="#fff" d="M6.6 10.8a15.1 15.1 0 0 0 6.6 6.6l2.2-2.2c.3-.3.7-.4 1-.2 1.1.4 2.3.6 3.6.6.6 0 1 .4 1 1V20c0 .6-.4 1-1 1A17 17 0 0 1 3 4c0-.6.4-1 1-1h3.5c.6 0 1 .4 1 1 0 1.3.2 2.5.6 3.6.1.3 0 .7-.2 1z"/></svg>
        </span>
        098 765 4321
      </li>
      <li class="contacts__item">
        <span class="contacts__icon">
          <svg width="14" height="14" viewBox="0 0 24 24" fill="none" stroke="#fff" stroke-width="2"><circle cx="12" cy="12" r="9"/><ellipse cx="12" cy="12" rx="4" ry="9"/><line x1="3" y1="12" x2="21" y2="12"/></svg>
        </span>
        www.nellharper.com
      </li>
      <li class="contacts__item">
        <span class="contacts__icon">
          <svg width="14" height="14" viewBox="0 0 24 24" fill="none" stroke="#fff" stroke-width="2.2"><circle cx="12" cy="12" r="4"/><path d="M16 12v1.5a2.5 2.5 0 0 0 5 0V12a9 9 0 1 0-3.5 7.1"/></svg>
        </span>
        nellharper@postbox.net
      </li>
    </ul>
  </section>
</main>
</body>
</html>
```